Marlowe Consulting Cover 1 - Hunting Funds Like Bibble Hunts the Gronket

Marlowe Consulting is a business consulting firm. We will publish a series of four thought leadership pieces online and via PDF. The first of the series is attached to this project. We need an eye-catching cover page with a back page that keeps with our branding. The document attached is in the final draft, and the cover and pack pages are placeholders only. You can find more about our branding and style on our website www.marloweconsulting.com.au. The other three projects can be found here with a similar brief, and you are welcome to submit a design for all 4.

```html
<!DOCTYPE html>
<html lang="en">
<head>
<meta charset="utf-8">
<title>Marlowe Consulting – Hunting Funds Like Bibble Hunts the Gronket</title>
<link rel="stylesheet" href="https://fonts.googleapis.com/css2?family=Poppins:wght@400;500;600;700&display=swap">
<style>
  :root {
    --ink: #323a45;
    --orange: #f7931e;
    --sky: #1ba8ea;
    --white: #ffffff;
    --paper: #ffffff;
  }
  * { margin: 0; padding: 0; box-sizing: border-box; }
  html, body { width: 1200px; height: 830px; overflow: hidden; background: var(--paper); }
  body { font-family: "Poppins", sans-serif; position: relative; }

  .page { position: absolute; top: 0; width: 586px; height: 830px; background: var(--ink); overflow: hidden; color: var(--white); }
  .page--cover { left: 0; }
  .page--back { left: 614px; }
  .page__shapes { position: absolute; inset: 0; width: 100%; height: 100%; }
  .page > *:not(.page__shapes) { position: absolute; }

  .brand { display: flex; align-items: center; gap: 12px; }
  .brand__dot { border-radius: 50%; background: var(--orange); flex: none; }
  .brand__name { font-weight: 600; color: var(--white); line-height: 1.05; }

  .cover__brand { left: 42px; top: 54px; }
  .cover__brand .brand__dot { width: 46px; height: 46px; }
  .cover__brand .brand__name { font-size: 18px; }

  .cover__title { left: 42px; top: 222px; }
  .cover__headline { font-size: 52px; font-weight: 700; color: var(--orange); line-height: 1.1; letter-spacing: -0.3px; }
  .cover__subline { font-size: 33px; font-weight: 600; line-height: 1.55; margin-top: 4px; }

  .web { display: flex; align-items: center; gap: 7px; font-size: 15px; font-weight: 500; }
  .web svg { width: 15px; height: 15px; }
  .cover__web { left: 280px; top: 784px; color: var(--white); }

  .back__brand { left: 42px; top: 34px; }
  .back__brand .brand__dot { width: 78px; height: 78px; }
  .back__brand .brand__name { font-size: 30px; }

  .back__heading { left: 42px; top: 172px; font-size: 36px; font-weight: 600; color: var(--orange); }
  .back__intro { left: 42px; top: 242px; font-size: 21px; font-weight: 500; line-height: 26.5px; }
  .back__intro strong { font-weight: 700; }

  .contact { left: 42px; }
  .contact--first { top: 346px; }
  .contact--second { top: 457px; }
  .contact__name { font-size: 22px; font-weight: 600; color: var(--orange); line-height: 1.2; }
  .contact__role { font-size: 12.5px; font-weight: 600; color: var(--sky); line-height: 1.3; margin-bottom: 8px; }
  .contact__line { font-size: 13px; line-height: 1.35; }

  .social { left: 42px; top: 786px; display: flex; align-items: center; gap: 14px; font-size: 12.5px; font-weight: 700; }
  .social__icon { width: 15px; height: 15px; border-radius: 50%; background: var(--white); }
  .back__web { left: 297px; top: 784px; color: var(--ink); }
</style>
</head>
<body>

<section class="page page--cover">
  <svg class="page__shapes" viewBox="0 0 420 595" preserveAspectRatio="none" aria-hidden="false">
    <defs>
      <linearGradient id="towerGrey" x1="0" y1="0" x2="1" y2="1">
        <stop offset="0" stop-color="#a9adb0"/><stop offset="1" stop-color="#6f7880"/>
      </linearGradient>
      <linearGradient id="glassBlue" x1="0" y1="0" x2="1" y2="1">
        <stop offset="0" stop-color="#5cb8e6"/><stop offset="1" stop-color="#2c8fcb"/>
      </linearGradient>
      <linearGradient id="cityWarm" x1="0" y1="0" x2="0" y2="1">
        <stop offset="0" stop-color="#c79a5e"/><stop offset="0.55" stop-color="#7a7a72"/><stop offset="1" stop-color="#3a6f9c"/>
      </linearGradient>
      <linearGradient id="stairsBlue" x1="0" y1="0" x2="1" y2="1">
        <stop offset="0" stop-color="#3fa0dc"/><stop offset="1" stop-color="#1d6fa8"/>
      </linearGradient>
    </defs>
    <polygon points="148,130 168,130 224,0 204,0" fill="var(--sky)"/>
    <polygon points="170,130 272,130 330,0 228,0" fill="url(#towerGrey)" role="img" aria-label="Photo of an office tower facade seen from below"/>
    <polygon points="280,130 420,130 420,0 338,0" fill="url(#glassBlue)" role="img" aria-label="Photo of a blue glass skyscraper"/>
    <polygon points="0,370 45,300 62,300 0,395" fill="var(--sky)"/>
    <polygon points="0,410 66,300 175,300 115,595 0,595" fill="url(#cityWarm)" role="img" aria-label="Photo of city towers in warm light"/>
    <polygon points="125,595 183,300 300,300 140,595" fill="url(#stairsBlue)" role="img" aria-label="Photo of a businessman standing on modern steps"/>
    <polygon points="420,140 420,150 210,545 204,540" fill="var(--white)"/>
    <polygon points="420,162 420,545 212,545" fill="var(--orange)"/>
  </svg>

  <div class="brand cover__brand">
    <span class="brand__dot"></span>
    <span class="brand__name">Marlowe<br>Consulting</span>
  </div>

  <h1 class="cover__title">
    <span class="cover__headline">Hunting Funds</span>
    <span class="cover__subline" style="display:block">Like Bibble Hunts<br>the Gronket</span>
  </h1>

  <div class="web cover__web">
    <svg viewBox="0 0 16 16" fill="none" stroke="currentColor" stroke-width="1.4"><circle cx="8" cy="8" r="6.5"/><ellipse cx="8" cy="8" rx="3" ry="6.5"/><line x1="1.5" y1="8" x2="14.5" y2="8"/></svg>
    marloweconsulting.com.au
  </div>
</section>

<section class="page page--back">
  <svg class="page__shapes" viewBox="0 0 420 595" preserveAspectRatio="none">
    <polygon points="293,90 360,90 382,45 318,45" fill="var(--sky)"/>
    <polygon points="312,80 420,80 420,37 338,37" fill="var(--orange)"/>
    <polygon points="420,115 420,124 148,595 139,595" fill="var(--white)"/>
    <polygon points="420,135 420,595 158,595" fill="var(--sky)"/>
  </svg>

  <div class="brand back__brand">
    <span class="brand__dot"></span>
    <span class="brand__name">Marlowe<br>Consulting</span>
  </div>

  <h2 class="back__heading">Contact us</h2>
  <p class="back__intro">Find out how <strong>Marlowe Consulting</strong><br>can help build your company<br>into a market leader today.</p>

  <div class="contact contact--first">
    <p class="contact__name">Edwin Marlowe</p>
    <p class="contact__role">Managing Director</p>
    <p class="contact__line">Mobile: +61 400 318 526</p>
    <p class="contact__line">Email: edwin@marloweconsulting.com.au</p>
  </div>

  <div class="contact contact--second">
    <p class="contact__name">Rupert Marlowe</p>
    <p class="contact__role">Managing Director</p>
    <p class="contact__line">Mobile: +61 400 624 917</p>
    <p class="contact__line">Email: rupert@marloweconsulting.com.au</p>
  </div>

  <div class="social">
    <span>Follow us</span>
    <span class="social__icon" aria-label="Social profile"></span>
    <span class="social__icon" aria-label="Social profile"></span>
  </div>

  <div class="web back__web">
    <svg viewBox="0 0 16 16" fill="none" stroke="currentColor" stroke-width="1.4"><circle cx="8" cy="8" r="6.5"/><ellipse cx="8" cy="8" rx="3" ry="6.5"/><line x1="1.5" y1="8" x2="14.5" y2="8"/></svg>
    marloweconsulting.com.au
  </div>
</section>

</body>
</html>
```